VIREMO DATA Business Card project

We need a Business Card design for a brand new company called VIREMO DATA, based in Colombia, South America. In spanish, the name VIREMO DATA is built from Describing a Story with Data (Describir UNA Historia con Datos).
We recently finished our new logo project and now we need the business cards.
In VIREMO we generate knowledge from data. By producing an INTELLIGENT VISUALIZATION of our clients´ data we create AWARENESS of their business environment. We drive GROWTH through DATA VISUALIZATION.
We are a service provider of Data Science, Business Intelligence and Visualization and we are breaking mental barriers in our culture and our market. It is an innovative way to use this services procuring mid term contracts to take our clients in a data based journey to understand their environment. We awe our clients with our data driven insights and our state of the art visualizations
We would like our clients to be seen as: Knowledgable, Dynamic, Fresh, Smart, Acute, Open minded, Brainy, Evolving
Our core has this 4 words: Visual, Knowledgable, Mathematician, Genius
Our brand personality is: Young (early 30s), Brainy, Easy going, Street smart, Creative, Mind blowing, Very Techie, Fun, Social, Uncomplicated
Our promise: we deliver data driven insights using state-of-the-art computer modeling and creative analysis.
This is the first step and the milestone to build all our graphic future (website, mail signature, banners, envelopes, Templates, etc)
It is a face to face sale with cloud based reports and visualizations
There is a similar company that has done great and we want to emulate but we must be different: www.qolstrix.co
Target Market(s)
Business Intelligence managers, Upper level management, General managers, IT heads and graphic designers
Industry/Entity Type
Computer
Look and feel
Each slider illustrates characteristics of the customer's brand and the style your logo design should communicate.

```html
<!DOCTYPE html>
<html lang="en">
<head>
<meta charset="utf-8">
<title>VIREMO DATA – Business Card</title>
<link rel="stylesheet" href="https://fonts.googleapis.com/css2?family=Montserrat:wght@500;600;700&display=swap">
<style>
  :root {
    --bg: #e4e4e4;
    --paper: #f4f4f2;
    --ink: #1a1a1a;
    --brand-ink: #3a3a3a;
    --orange: #f08a1c;
    --white: #ffffff;
  }
  * { margin: 0; padding: 0; box-sizing: border-box; }
  html, body { width: 976px; height: 1200px; overflow: hidden; }
  body {
    background: var(--bg);
    font-family: "Montserrat", Arial, sans-serif;
    position: relative;
  }
  .card {
    position: absolute;
    left: 138px;
    width: 700px;
    height: 400px;
    background: var(--paper);
    box-shadow: 0 10px 30px rgba(0,0,0,0.18);
    overflow: hidden;
  }
  .card--front { top: 150px; }
  .card--back { top: 650px; }

  .front-panel { position: absolute; inset: 0; }

  .brand {
    position: absolute;
    display: flex;
    align-items: center;
    gap: 12px;
    color: var(--brand-ink);
    font-weight: 600;
    letter-spacing: 1px;
    white-space: nowrap;
  }
  .brand__mark {
    background: var(--orange);
    flex: none;
  }
  .card--front .brand { left: 36px; top: 178px; font-size: 28px; }
  .card--front .brand__mark { width: 18px; height: 18px; }
  .card--back .brand {
    left: 0; right: 0; top: 172px; justify-content: center; font-size: 48px; gap: 16px;
  }
  .card--back .brand__mark { width: 28px; height: 28px; }

  .contact {
    position: absolute;
    left: 372px;
    top: 54px;
    color: var(--white);
  }
  .contact__name {
    color: var(--orange);
    font-size: 30px;
    font-weight: 700;
    line-height: 1;
  }
  .contact__role {
    text-align: right;
    font-size: 12px;
    font-weight: 700;
    letter-spacing: 0.5px;
    margin-top: 2px;
  }
  .contact__list {
    list-style: none;
    margin-top: 28px;
  }
  .contact__item {
    display: flex;
    align-items: center;
    gap: 18px;
    font-size: 14px;
    font-weight: 600;
    height: 28px;
  }
  .contact__icon { width: 18px; height: 18px; flex: none; }
</style>
</head>
<body>

<section class="card card--front" aria-label="Business card front">
  <svg class="front-panel" viewBox="0 0 700 400" aria-hidden="true">
    <path d="M305 0 H700 V400 H205 Q370 230 305 0 Z" fill="var(--ink)"/>
    <path d="M305 0 Q370 230 205 400" fill="none" stroke="var(--orange)" stroke-width="5"/>
  </svg>

  <div class="brand">
    <span class="brand__mark"></span>
    <span class="brand__name">VIREMO DATA</span>
  </div>

  <div class="contact">
    <p class="contact__name">Marta Quiroga</p>
    <p class="contact__role">OWNER</p>
    <ul class="contact__list">
      <li class="contact__item">
        <svg class="contact__icon" viewBox="0 0 24 24"><path d="M6 3l3 4-2 2c1 3 4 6 7 7l2-2 4 3-2 4C10 21 3 14 3 5z" fill="var(--orange)"/></svg>
        <span>581-204-376</span>
      </li>
      <li class="contact__item">
        <svg class="contact__icon" viewBox="0 0 24 24"><rect x="2" y="5" width="20" height="14" fill="var(--orange)"/><path d="M2 5l10 8 10-8M2 19l7-7M22 19l-7-7" stroke="var(--ink)" stroke-width="1.6" fill="none"/></svg>
        <span>hola@viremodata.co</span>
      </li>
      <li class="contact__item">
        <svg class="contact__icon" viewBox="0 0 24 24"><circle cx="12" cy="12" r="10" fill="var(--orange)"/><path d="M2 12h20M12 2v20M5 6c4 2 10 2 14 0M5 18c4-2 10-2 14 0" stroke="var(--ink)" stroke-width="1.2" fill="none"/></svg>
        <span>www.viremodata.co</span>
      </li>
      <li class="contact__item">
        <svg class="contact__icon" viewBox="0 0 24 24"><path d="M12 2a7 7 0 0 1 7 7c0 5-7 13-7 13S5 14 5 9a7 7 0 0 1 7-7z" fill="var(--orange)"/><circle cx="12" cy="9" r="2.6" fill="var(--ink)"/></svg>
        <span>Address will be here</span>
      </li>
    </ul>
  </div>
</section>

<section class="card card--back" aria-label="Business card back">
  <div class="brand">
    <span class="brand__mark"></span>
    <span class="brand__name">VIREMO DATA</span>
  </div>
</section>

</body>
</html>
```